Velvet Lantern rebranding my business with a new business card

I have my new logo and now I need a refresher on my business cards. I really want something fun and fresh. I like black background or anything to make the color pop.
Logo
Name: Velvet Lantern
Contact Info as stated below:
Mara Pelkin
519-555-0147
Logo
Name: Velvet Lantern
Mara Pelkin
519-555-0147
vl.page/VelvetLantern
Instagram: @VelvetLanternbyMara

Industry/Entity Type

Business

Contact Information for Business Card

double-sided. Logo on one side. Contact info on the other.

Requirements
Must have
• Logo
• Name: Velvet Lantern
• Contact Info as stated below:
• Mara Pelkin
• 519-555-0147
• vl.page/VelvetLantern
• vl.page/VelvetLantern

```html
<!DOCTYPE html>
<html lang="en">
<head>
<meta charset="utf-8">
<title>Velvet Lantern – Business Card</title>
<link href="https://fonts.googleapis.com/css2?family=Open+Sans:wght@400;600&display=swap" rel="stylesheet">
<style>
  :root {
    --page-bg: #eeecea;
    --card-teal: #6ecdc0;
    --card-pink: #fbc3c4;
    --ink: #1d2626;
    --badge-white: #ffffff;
    --badge-shade: #e3e7e8;
  }
  html, body {
    margin: 0;
    padding: 0;
    width: 1200px;
    height: 900px;
    overflow: hidden;
    background: var(--page-bg);
    font-family: "Open Sans", sans-serif;
  }
  .business-card {
    position: absolute;
    left: 150px;
    top: 173px;
    width: 900px;
    height: 554px;
    border-radius: 19px;
    overflow: hidden;
    background: linear-gradient(to right, var(--card-teal) 0 648px, var(--card-pink) 648px 100%);
    color: var(--ink);
    box-shadow: 0 10px 30px rgba(0,0,0,0.12);
  }
  .owner-name {
    position: absolute;
    left: 55px;
    top: 50px;
    margin: 0;
    font-size: 31px;
    font-weight: 600;
    letter-spacing: 0.5px;
    text-transform: uppercase;
  }
  .contact-list {
    position: absolute;
    left: 55px;
    top: 315px;
    margin: 0;
    padding: 0;
    list-style: none;
    font-size: 22px;
    line-height: 35px;
  }
  .contact-list li,
  .social-handle {
    display: flex;
    align-items: center;
  }
  .contact-icon {
    width: 18px;
    height: 18px;
    margin-right: 14px;
    fill: var(--ink);
  }
  .social-handle {
    position: absolute;
    left: 48px;
    top: 466px;
    font-size: 23px;
  }
  .social-dot {
    width: 33px;
    height: 33px;
    border-radius: 50%;
    background: var(--ink);
    margin-right: 11px;
  }
  .logo-badge {
    position: absolute;
    left: 392px;
    top: 36px;
    width: 476px;
    height: 476px;
    border-radius: 50%;
    background: radial-gradient(circle at 40% 35%, var(--badge-white) 0%, var(--badge-white) 45%, var(--badge-shade) 100%);
    display: flex;
    align-items: center;
    justify-content: center;
  }
  .brand-name {
    font-size: 44px;
    font-weight: 600;
    color: var(--ink);
    letter-spacing: 1px;
  }
</style>
</head>
<body>
  <div class="business-card">
    <h1 class="owner-name">Mara Pelkin</h1>

    <ul class="contact-list">
      <li>
        <svg class="contact-icon" viewBox="0 0 20 20" aria-hidden="true">
          <path d="M2 7c0-3 3-5 8-5s8 2 8 5v1h-4V6.5c-1-.6-2.3-.9-4-.9s-3 .3-4 .9V8H2z"/>
          <path d="M5 9h10l2 8H3z M10 11a2.5 2.5 0 1 0 0 5a2.5 2.5 0 0 0 0-5z"/>
        </svg>
        519-555-0147
      </li>
      <li>
        <svg class="contact-icon" viewBox="0 0 20 20" aria-hidden="true">
          <path d="M2 4h16v12H2z M3.5 5.5v.6l6.5 5 6.5-5v-.6z" fill-rule="evenodd"/>
        </svg>
        info@velvetlanternmail.com
      </li>
      <li>
        <svg class="contact-icon" viewBox="0 0 20 20" aria-hidden="true">
          <circle cx="10" cy="10" r="8"/>
          <path d="M2 10h16M10 2c-3 3-3 13 0 16M10 2c3 3 3 13 0 16" stroke="#6ecdc0" stroke-width="1.3" fill="none"/>
        </svg>
        www.velvetlanternweb.com
      </li>
    </ul>

    <div class="social-handle">
      <span class="social-dot" aria-hidden="true"></span>
      vl.page/VelvetLantern
    </div>

    <div class="logo-badge">
      <span class="brand-name">Velvet Lantern</span>
    </div>
  </div>
</body>
</html>
```